Marrow Vance Fine Art gallery website - Modern british art for sale

We need a website design that is both current and high end. Our products are expensive and this should be reflected in the look of the website. We would like the logo we had designed last year to be clearly seen in the design. We want sleek, simple, and easy to navigate. Nothing too colourful as the colours of the art should always take precedence.

Target Market(s)

The average price of one our products starts at £250 and can go up to £10,000 we are an entry level gallery.

Industry/Entity Type

Art Gallery

Number of Pages Required

5+ page

Font styles to use
Sans Serif

Colors
000000
ffffff
faa54b
abd037
886aae
b868aa

Requirements
Must have
• Attractive front page. Linked to our Twitter feed.
• 4 links from front page - New Releases, about us, Artists, contact us
• Social media links - Facebook, Twitter, YouTube, Instagram.
• Each artist must have their own page, each page must have a biography link to another page.
Nice to have
• Utilise our new logo design. I would like the Twitter feed to link to the front page in a small way so you can see what's being said on Twitter by the company. For future proofing maybe have a locations function on the front page which can be adroit down menu showing where our other galleries are.

```html
<!DOCTYPE html>
<html lang="en">
<head>
<meta charset="utf-8">
<title>Marrow Vance Fine Art</title>
<link rel="stylesheet" href="https://fonts.googleapis.com/css2?family=Cinzel:wght@400;600&family=Lato:wght@400;700&display=swap">
<style>
:root{
  --ink:#000000;
  --paper:#ffffff;
  --wood:#151515;
  --panel:#f2f2f2;
  --text:#222222;
  --muted:#b5b5b5;
  --gold:#c9a24a;
}
*{margin:0;padding:0;box-sizing:border-box}
html,body{width:1200px;height:2782px;overflow:hidden;background:var(--paper)}
body{position:relative;font-family:"Lato",sans-serif;color:var(--text)}
.abs{position:absolute}

/* header */
.site-header{left:0;top:0;width:1200px;height:117px;background:linear-gradient(180deg,#2a2a2a,#111)}
.brand{left:80px;top:36px;display:flex;align-items:center;gap:14px;color:var(--paper);font-family:"Cinzel",serif;font-size:30px;letter-spacing:1px;white-space:nowrap}
.brand-mark{width:14px;height:14px;border-radius:50%;background:var(--gold)}
.contact{top:20px;display:flex;align-items:center;gap:14px;color:var(--paper);font-size:17px;white-space:nowrap}
.contact svg{width:30px;height:30px}
.main-nav{top:74px;left:0;width:1200px}
.main-nav a{position:absolute;color:var(--paper);text-decoration:none;font-family:"Cinzel",serif;font-size:15px;letter-spacing:.5px;white-space:nowrap}

/* hero */
.hero{left:0;top:117px;width:1200px;height:495px;background:linear-gradient(120deg,#d8421c 0%,#f0a72a 22%,#2a6ab8 45%,#8a3e28 62%,#e2482a 80%,#29a0c8 100%)}
.hero-dots{left:595px;top:576px;display:flex;gap:6px}
.hero-dots span{width:9px;height:9px;border-radius:50%;background:#ddd}

/* section headings */
.heading{left:0;width:1200px;text-align:center;font-family:"Cinzel",serif;letter-spacing:2px}
.divider{left:395px;width:410px;height:24px}

/* gallery intro */
.gallery-intro{left:0;top:612px;width:1200px;height:269px;background:var(--ink)}
.tab{top:781px;height:41px;line-height:39px;color:var(--paper);font-size:20px;font-weight:700;letter-spacing:1.2px;text-align:center;white-space:nowrap}
.tab.active{left:434px;width:176px;border:1.5px solid var(--paper)}
.tab.active::after{content:"";position:absolute;left:83px;bottom:-8px;border:5px solid transparent;border-top:6px solid var(--paper)}
.tab.specials{left:650px;width:140px}

/* gallery wall */
.gallery-wall{left:0;top:881px;width:1200px;height:931px;background:repeating-linear-gradient(90deg,#141414 0 40px,#1c1c1c 40px 52px,#111 52px 110px,#191919 110px 130px)}
.frame{background:var(--paper);padding:18px;box-shadow:0 0 0 6px #2a2a2a}
.art{width:100%;height:100%}
.caption{left:48px;top:165px;padding-left:20px;border-left:1.5px solid var(--paper);color:var(--paper)}
.caption h3{font-size:15px;font-weight:700;letter-spacing:.5px;padding-bottom:10px;margin-bottom:10px;position:relative}
.caption h3::after{content:"";position:absolute;left:0;bottom:0;width:38px;height:1.5px;background:var(--paper)}
.caption p{font-size:15px;line-height:24px;color:#ddd}

/* artist */
.artist-photo{left:0;top:1812px;width:542px;height:364px;background:linear-gradient(110deg,#e8e2da,#f3c9a0 45%,#4a90c8 75%,#f2d24a)}
.artist-panel{left:542px;top:1812px;width:658px;height:364px;background:var(--panel)}
.artist-name{left:586px;top:1843px;font-family:"Cinzel",serif;font-size:29px;font-weight:600;color:#111;letter-spacing:1px}
.artist-bio{left:586px;top:1943px;width:535px;font-size:13.5px;line-height:22px;color:#222}
.pager{left:1070px;top:2124px;width:50px;height:12px}

/* feed */
.feed-post{width:500px;height:90px}
.avatar{left:0;top:0;width:96px;height:80px}
.feed-body{left:115px;top:0;width:385px}
.feed-body h4{font-size:14.5px;font-weight:700;color:#111;display:flex;align-items:center;gap:10px;margin-bottom:4px;white-space:nowrap}
.feed-body h4 i{display:inline-block;width:12px;height:12px;border-radius:50%;background:var(--muted)}
.feed-body p{font-size:13px;line-height:19.5px;color:#222}

/* footer */
.site-footer{left:0;top:2590px;width:1200px;height:192px;background:#0b0b0b}
.footer-nav a{position:absolute;top:2626px;color:var(--paper);text-decoration:none;font-size:13px;font-weight:700;letter-spacing:.5px;white-space:nowrap}
.social{left:532px;top:2674px;display:flex;gap:12px}
.social a{width:24px;height:24px;background:#3a3a3a;border-radius:2px}
.copyright{left:0;top:2726px;width:1200px;text-align:center;color:var(--paper);font-size:12px}
</style>
</head>
<body>

<header class="site-header abs">
  <div class="brand abs"><span class="brand-mark"></span>Marrow Vance Fine Art</div>
  <div class="contact abs" style="left:762px">
    <svg viewBox="0 0 30 30" fill="none" stroke="#fff" stroke-width="2"><circle cx="15" cy="15" r="12"/><path d="M15 8v7l5 3"/></svg>
    10:30 am-5:30 pm
  </div>
  <div class="contact abs" style="left:968px">
    <svg viewBox="0 0 30 30" fill="none" stroke="#fff" stroke-width="2"><circle cx="15" cy="15" r="12"/><path d="M11 9l2 0 1 3-1.5 1a7 7 0 0 0 3.5 3.5l1-1.5 3 1v2c0 1-1 1.5-2 1.5a10 10 0 0 1-8.5-8.5c0-1 .5-2 1.5-2z" fill="#fff" stroke="none"/></svg>
    020-555-0143
  </div>
  <nav class="main-nav abs">
    <a href="#" style="left:584px">NEW RELEASES</a>
    <a href="#" style="left:760px">ABOUT US</a>
    <a href="#" style="left:903px">ARTISTS</a>
    <a href="#" style="left:1028px">LOCATIONS</a>
  </nav>
</header>

<section class="hero abs" role="img" aria-label="Vivid palette-knife painting of a woman playing the cello"></section>
<div class="hero-dots abs"><span></span><span></span></div>

<section class="gallery-intro abs"></section>
<h2 class="heading abs" style="top:652px;color:var(--paper);font-size:40px;font-weight:400">GALLERY</h2>
<svg class="divider abs" style="top:713px" viewBox="0 0 410 24">
  <line x1="0" y1="12" x2="182" y2="12" stroke="#777"/>
  <line x1="228" y1="12" x2="410" y2="12" stroke="#777"/>
  <rect x="196" y="3" width="18" height="18" transform="rotate(45 205 12)" fill="none" stroke="#aaa"/>
  <rect x="201" y="8" width="8" height="8" transform="rotate(45 205 12)" fill="#aaa"/>
  <circle cx="188" cy="12" r="2" fill="#aaa"/><circle cx="222" cy="12" r="2" fill="#aaa"/>
</svg>
<div class="tab active abs">NEW ARRIVALS</div>
<div class="tab specials abs">SPECIALS</div>

<section class="gallery-wall abs"></section>
<div class="frame abs" style="left:89px;top:979px;width:477px;height:462px">
  <div class="art" style="background:#2b2b2b;position:relative" role="img" aria-label="Dark charcoal sketch of riders on horseback">
    <div class="caption abs">
      <h3>LOREN IPSUM DOLOR</h3>
      <p>consectetuer adipiscing elit<br>£ 250.00</p>
    </div>
  </div>
</div>
<div class="frame abs" style="left:636px;top:979px;width:477px;height:212px">
  <div class="art" role="img" aria-label="Painting of a white farmhouse with a well sweep under a blue sky" style="background:linear-gradient(180deg,#9fb7c8 0%,#c9d0c4 45%,#7a6a3e 70%,#6e7a3a 100%)"></div>
</div>
<div class="frame abs" style="left:636px;top:1228px;width:477px;height:213px">
  <div class="art" role="img" aria-label="Abstract oval split into navy and yellow halves with coloured stripes" style="background:linear-gradient(90deg,#dcebf3 0 10%,#2e3a7a 10% 40%,#c46a9a 40% 55%,#e3b21c 55% 90%,#dcebf3 90%)"></div>
</div>
<div class="frame abs" style="left:89px;top:1488px;width:477px;height:226px">
  <div class="art" role="img" aria-label="Abstract pattern of orange, lilac and olive wave shapes" style="background:linear-gradient(110deg,#f27a4a,#b48ad8 35%,#cfc36a 60%,#f27a4a)"></div>
</div>
<div class="frame abs" style="left:636px;top:1488px;width:214px;height:226px">
  <div class="art" role="img" aria-label="Painting of red birds on wintry branches" style="background:radial-gradient(circle at 50% 60%,#e2502a,#3a3a48 70%)"></div>
</div>
<div class="frame abs" style="left:900px;top:1488px;width:213px;height:226px">
  <div class="art" role="img" aria-label="Dark moody landscape at dusk" style="background:linear-gradient(180deg,#8a7a4a,#3a3420 60%,#1e1a10)"></div>
</div>

<section class="artist-photo abs" role="img" aria-label="Smiling painter holding brushes and a palette beside paint bottles"></section>
<section class="artist-panel abs"></section>
<h2 class="artist-name abs">CLARA WHITBY</h2>
<svg class="abs" style="left:586px;top:1899px;width:535px;height:24px" viewBox="0 0 535 24">
  <rect x="5" y="5" width="14" height="14" transform="rotate(45 12 12)" fill="none" stroke="#ccc"/>
  <line x1="26" y1="12" x2="535" y2="12" stroke="#d4d4d4"/>
</svg>
<p class="artist-bio abs">Lorem ipsum dolor sit amet, consectetuer adipiscing elit, sed diam nonummy nibh euismod tincidunt ut laoreet dolore magna aliquam erat volutpat. Ut wisi enim ad minim veniam, quis nostrud exerci tation ullamcorper suscipit lobortis nisl ut aliquip ex ea commodo consequat. Duis autem vel eum iriure dolor in hendrerit in vulputate velit esse molestie consequat, vel illum dolore eu feugiat nulla facilisis at vero eros et accumsan et iusto odio dignissim qui blandit praesent luptatum zzril delenit augue duis dolore te feugait nulla facilisi.</p>
<svg class="pager abs" viewBox="0 0 50 12" fill="none" stroke="#bbb">
  <rect x="2" y="2" width="8" height="8" transform="rotate(45 6 6)"/>
  <rect x="19" y="2" width="8" height="8" transform="rotate(45 23 6)"/>
  <rect x="36" y="2" width="8" height="8" transform="rotate(45 40 6)"/>
</svg>

<h2 class="heading abs" style="top:2212px;color:#111;font-size:40px;font-weight:600">LATEST FEEDS</h2>
<svg class="divider abs" style="top:2275px" viewBox="0 0 410 24">
  <line x1="0" y1="12" x2="190" y2="12" stroke="#ccc"/>
  <line x1="220" y1="12" x2="410" y2="12" stroke="#ccc"/>
  <rect x="198" y="5" width="14" height="14" transform="rotate(45 205 12)" fill="none" stroke="#bbb"/>
  <rect x="202" y="9" width="6" height="6" transform="rotate(45 205 12)" fill="#bbb"/>
</svg>

<article class="feed-post abs" style="left:82px;top:2341px">
  <div class="avatar abs" role="img" aria-label="Profile photo of a painter at work" style="background:linear-gradient(135deg,#8a7a6a,#c8b8a0)"></div>
  <div class="feed-body abs"><h4><i></i>Owen Hale @ohale</h4><p>Lorem ipsum dolor sit amet, consectetuers, jg adipiscing elit, nonummy nibhjhi vmo euismod tincidunt ut laoreet dolore.jg adipiscing elit,</p></div>
</article>
<article class="feed-post abs" style="left:651px;top:2341px">
  <div class="avatar abs" role="img" aria-label="Profile photo of colourful paintings" style="background:linear-gradient(135deg,#3a8ac8,#e2c04a,#c84a3a)"></div>
  <div class="feed-body abs"><h4><i></i>Quiet Heron @quiet Heron</h4><p>Lorem ipsum dolor sit amet, consectetuers, jg adipiscing elit, nonummy nibhjhi vmo euismod tincidunt ut laoreet dolore.jg adipiscing elit,</p></div>
</article>
<article class="feed-post abs" style="left:82px;top:2454px">
  <div class="avatar abs" role="img" aria-label="Profile photo of a child painting" style="background:linear-gradient(135deg,#e2a23a,#c84a2a,#3a6ac8)"></div>
  <div class="feed-body abs"><h4><i></i>Nora Fenwick @nfenwick</h4><p>Lorem ipsum dolor sit amet, consectetuers, jg adipiscing elit, nonummy nibhjhi vmo euismod tincidunt ut laoreet dolore.jg adipiscing elit,</p></div>
</article>
<article class="feed-post abs" style="left:651px;top:2454px">
  <div class="avatar abs" role="img" aria-label="Profile portrait photo" style="background:linear-gradient(135deg,#dfe6ec,#b8c4d0)"></div>
  <div class="feed-body abs"><h4><i></i>Ravi Mehta @ravimeh</h4><p>Lorem ipsum dolor sit amet, consectetuers, jg adipiscing elit, nonummy nibhjhi vmo euismod tincidunt ut laoreet dolore.jg adipiscing elit,</p></div>
</article>

<footer class="site-footer abs"></footer>
<nav class="footer-nav">
  <a href="#" style="left:341px">NEW RELEASES</a>
  <a href="#" style="left:512px">ABOUT US</a>
  <a href="#" style="left:649px">ARTISTS</a>
  <a href="#" style="left:785px">LOCATIONS</a>
</nav>
<div class="social abs" aria-label="Social links"><a href="#" aria-label="Social link one"></a><a href="#" aria-label="Social link two"></a><a href="#" aria-label="Social link three"></a><a href="#" aria-label="Social link four"></a></div>
<p class="copyright abs">Copyright © 2017 Marrow Vance Fine Arts. All Righrd Reserved</p>

</body>
</html>
```